Fancy&Artistic design bussiness card!

I want a business card for myself.I'm a cinephile.Love watching SF(especially distopia one),Cult(mostly from midnight movies),Chivalrous story film. My favorite film for example,○Lantern (directed by morris Pembleton)○grubs○lord of clocks○wild copper canal(Japanese film)○noonday bend○tinmarsh ○wraith of the orchard ○SOTEL○the revenge of the buried crowd ○El topoAnd I also love modern art. I love their way of using colors(Glen Podmore,Lionel Budrick, Vallombri,etc..)I want to get a business card which is full of creativity, uniqueness and humor(related to movie or art would be much better).I will be very pleased if you would meet my expectations. Thank you.
Industry/Entity Type
Movie
Contact Information for Business Card
Name: HIROKAZU ENOMOTOAddress: 418 E62nd Avenue #5217 NewYork,NY 10024e-mail: Tadakuri@mailvex.com

```html
<!DOCTYPE html>
<html lang="en">
<head>
<meta charset="utf-8">
<title>Tadamasa Kuribaya — Business Card</title>
<link href="https://fonts.googleapis.com/css2?family=Cinzel:wght@400&family=Arimo:wght@400&display=swap" rel="stylesheet">
<style>
  :root {
    --backdrop: #e4e1dc;
    --ink-black: #070707;
    --teal-deep: #0a5b79;
    --teal-mid: #1f89a8;
    --teal-light: #4aaac4;
    --paper-white: #f4f8fa;
    --reel-silver: #b9c2c8;
    --reel-shadow: #5d6b73;
  }
  * { margin: 0; padding: 0; box-sizing: border-box; }
  html, body { width: 1200px; height: 1023px; overflow: hidden; }
  body {
    background: var(--backdrop);
    display: flex;
    flex-direction: column;
    align-items: center;
    justify-content: center;
    gap: 60px;
  }
  .card {
    position: relative;
    width: 700px;
    height: 400px;
    border-radius: 4px;
    overflow: hidden;
    box-shadow: 0 10px 30px rgba(0,0,0,0.25);
    background: radial-gradient(ellipse at 45% 60%, var(--teal-light) 0%, var(--teal-mid) 45%, var(--teal-deep) 100%);
    color: var(--paper-white);
  }
  .card__wave { position: absolute; inset: 0; width: 100%; height: 100%; }
  .reel-art {
    position: absolute;
    border-radius: 50%;
    background: radial-gradient(circle at 40% 40%, var(--paper-white) 0%, var(--reel-silver) 45%, var(--reel-shadow) 100%);
    opacity: 0.9;
  }
  .card--front .reel-art { left: 380px; top: 30px; width: 300px; height: 180px; }
  .card--back .reel-art { left: 150px; top: 40px; width: 300px; height: 150px; }
  .holder-name {
    position: absolute;
    font-family: "Cinzel", serif;
    font-weight: 400;
    letter-spacing: 2px;
    white-space: nowrap;
  }
  .card--front .holder-name { left: 220px; top: 222px; font-size: 30px; }
  .card--back .holder-name { left: 300px; top: 250px; font-size: 32px; }
  .holder-title, .contact-line {
    position: absolute;
    font-family: "Arimo", sans-serif;
    font-size: 17px;
    white-space: nowrap;
  }
  .holder-title { left: 232px; top: 264px; }
  .contact-line--street { left: 300px; top: 302px; }
  .contact-line--city { left: 300px; top: 326px; }
  .contact-line--email { left: 330px; top: 358px; }
  .mail-icon { position: absolute; left: 300px; top: 358px; width: 20px; height: 18px; }
</style>
</head>
<body>
  <section class="card card--front">
    <svg class="card__wave" viewBox="0 0 700 400" aria-hidden="true">
      <path d="M0 0 H250 C170 110 70 150 100 260 C118 330 150 370 165 400 H0 Z" fill="var(--ink-black)"/>
      <path d="M250 0 C170 110 70 150 100 260 C118 330 150 370 165 400" fill="none" stroke="var(--paper-white)" stroke-width="4"/>
    </svg>
    <div class="reel-art" role="img" aria-label="Illustration of two silver film reels with a strip of film unwinding"></div>
    <h1 class="holder-name">TADAMASA KURIBAYA</h1>
    <p class="holder-title">Your Title</p>
    <p class="contact-line contact-line--street">418 E62nd Avenue</p>
    <p class="contact-line contact-line--city">5217 NewYork,NY 10391e</p>
    <svg class="mail-icon" viewBox="0 0 20 18" aria-hidden="true">
      <rect x="1" y="3" width="18" height="12" rx="2" fill="var(--paper-white)"/>
      <path d="M2 4 L10 10 L18 4" fill="none" stroke="var(--teal-mid)" stroke-width="1.5"/>
    </svg>
    <p class="contact-line contact-line--email">Tadakuri@mailvex.com</p>
  </section>

  <section class="card card--back">
    <div class="reel-art" role="img" aria-label="Illustration of two silver film reels joined by a strip of film"></div>
    <h2 class="holder-name">TADAMASA KURIBAYA</h2>
  </section>
</body>
</html>
```